Flyer-Design für den Verkauf von Babyalben
Zielgruppe
Familien und Verwandte die gerade ein Baby bekommen haben - Flyer soll für den Verkauf von Babyalbum sein
Aufgabenstellung
Wenn aus Liebe Leben wird, bekommt das Glück einen Namen „
individuell gestaltetes Babyalbum mit Ergänzung privater Unterlagen und Namen

```html
<!DOCTYPE html>
<html lang="de">
<head>
<meta charset="utf-8">
<title>Babyalbum – Kostbare Momente</title>
<link href="https://fonts.googleapis.com/css2?family=Josefin+Sans:wght@400;600&family=Lora:wght@700&display=swap" rel="stylesheet">
<style>
  :root {
    --paper: #f7f7f6;
    --band: #b2e0df;
    --teal: #6ccbbf;
    --orange: #f5a449;
    --pink: #f08b8b;
    --blue: #379fd9;
    --grey: #676d71;
    --skin: #f6cfa1;
    --skin-edge: #e6b484;
  }
  * { margin: 0; padding: 0; box-sizing: border-box; }
  html, body { width: 1200px; height: 800px; overflow: hidden; background: var(--paper); }
  .flyer {
    position: relative;
    width: 1200px;
    height: 800px;
    background: var(--paper);
    overflow: hidden;
  }
  .confetti-area {
    position: absolute;
    left: 0;
    width: 1200px;
    background: linear-gradient(90deg, rgba(240,139,139,0.10), rgba(108,203,191,0.12), rgba(245,164,73,0.10), rgba(240,139,139,0.10));
  }
  .confetti-top { top: 0; height: 95px; }
  .confetti-mid { top: 215px; height: 120px; }
  .top-band {
    position: absolute;
    top: 95px;
    left: 0;
    width: 1200px;
    height: 100px;
    background: var(--band);
  }
  .band-word {
    position: absolute;
    top: 127px;
    font-family: "Josefin Sans", sans-serif;
    font-weight: 400;
    font-size: 38px;
    letter-spacing: 0.22em;
    color: var(--grey);
    line-height: 1;
  }
  .band-word.left { left: 112px; }
  .band-word.right { right: 112px; }
  .pacifier {
    position: absolute;
    top: 120px;
    width: 44px;
    height: 52px;
    border-radius: 50% 50% 45% 45%;
  }
  .pacifier.left { left: 36px; background: linear-gradient(160deg, var(--orange) 30%, var(--blue) 31%); }
  .pacifier.right { right: 36px; background: linear-gradient(160deg, var(--orange) 30%, var(--pink) 31%); }
  .baby-portrait {
    position: absolute;
    left: 485px;
    top: 48px;
    width: 220px;
    height: 200px;
    border-radius: 50%;
    background: radial-gradient(circle at 50% 45%, var(--skin) 70%, var(--skin-edge) 100%);
    border: 5px solid var(--paper);
  }
  .title {
    position: absolute;
    left: 0;
    width: 1200px;
    text-align: center;
    font-family: "Lora", serif;
    font-weight: 700;
    line-height: 1;
  }
  .title.main { top: 380px; font-size: 112px; color: var(--teal); }
  .title.sub { top: 540px; font-size: 104px; color: var(--orange); letter-spacing: 0.01em; }
  .footer-band {
    position: absolute;
    left: 0;
    bottom: 0;
    width: 1200px;
    height: 88px;
    background: var(--band);
  }
  .hearts {
    position: absolute;
    top: 20px;
    display: flex;
    gap: 26px;
  }
  .hearts.left { left: 70px; }
  .hearts.right { right: 90px; }
  .heart { width: 60px; height: 52px; }
  .web-address {
    position: absolute;
    left: 0;
    width: 1200px;
    top: 28px;
    display: flex;
    justify-content: center;
    align-items: center;
    gap: 12px;
    font-family: "Josefin Sans", sans-serif;
    font-weight: 600;
    font-size: 26px;
    letter-spacing: 0.18em;
    color: var(--grey);
  }
  .brand-dot {
    width: 16px;
    height: 16px;
    border-radius: 50%;
    background: var(--grey);
  }
</style>
</head>
<body>
<main class="flyer">
  <div class="confetti-area confetti-top" role="img" aria-label="Verstreute bunte Konfetti-Punkte"></div>
  <div class="confetti-area confetti-mid" role="img" aria-label="Verstreute bunte Konfetti-Punkte"></div>

  <div class="top-band"></div>
  <div class="pacifier left" role="img" aria-label="Illustration eines blauen Schnullers"></div>
  <span class="band-word left">INDIVIDUELL</span>
  <div class="baby-portrait" role="img" aria-label="Illustration eines lächelnden Babykopfes"></div>
  <span class="band-word right">LIEBEVOLL</span>
  <div class="pacifier right" role="img" aria-label="Illustration eines roten Schnullers"></div>

  <h1 class="title main">Babyalbum</h1>
  <p class="title sub">"Kostbare Momente"</p>

  <footer class="footer-band">
    <div class="hearts left">
      <svg class="heart" viewBox="0 0 60 52"><path fill="var(--pink)" d="M30 50 C8 34 2 24 2 15 A14 14 0 0 1 30 10 A14 14 0 0 1 58 15 C58 24 52 34 30 50Z"/></svg>
      <svg class="heart" viewBox="0 0 60 52"><path fill="var(--orange)" d="M30 50 C8 34 2 24 2 15 A14 14 0 0 1 30 10 A14 14 0 0 1 58 15 C58 24 52 34 30 50Z"/></svg>
      <svg class="heart" viewBox="0 0 60 52"><path fill="var(--blue)" d="M30 50 C8 34 2 24 2 15 A14 14 0 0 1 30 10 A14 14 0 0 1 58 15 C58 24 52 34 30 50Z"/></svg>
    </div>
    <div class="web-address">
      <span>www.</span><span class="brand-dot"></span><span>Albumhaus</span><span>.eu</span>
    </div>
    <div class="hearts right">
      <svg class="heart" viewBox="0 0 60 52"><path fill="var(--blue)" d="M30 50 C8 34 2 24 2 15 A14 14 0 0 1 30 10 A14 14 0 0 1 58 15 C58 24 52 34 30 50Z"/></svg>
      <svg class="heart" viewBox="0 0 60 52"><path fill="var(--orange)" d="M30 50 C8 34 2 24 2 15 A14 14 0 0 1 30 10 A14 14 0 0 1 58 15 C58 24 52 34 30 50Z"/></svg>
      <svg class="heart" viewBox="0 0 60 52"><path fill="var(--pink)" d="M30 50 C8 34 2 24 2 15 A14 14 0 0 1 30 10 A14 14 0 0 1 58 15 C58 24 52 34 30 50Z"/></svg>
    </div>
  </footer>
</main>
</body>
</html>
```